KVT Business Cards

We require business cards for our business. We would like a matte black back to the card, with our logo centred in the middle. The front side of the card is open to design.

Target Market(s)

Clients looking for legal services (professional)

Industry/Entity Type

Legal

Contact Information for Business Card

Boris Telemark
Partner
Mobile: 0438 715 642
Email: boris@kvtlaw.co
Website: www.kvtlaw.co
Level 3, 118 Wexbury Street
Sydney NSW 2000

Font styles to use
Other font styles liked:
• Avenir

Colors
f04a50
ffffff
1b1b1b

Requirements
Must have
• Black back with logo included in the centre of the card.
• Our font is Avenir.

```html
<!DOCTYPE html>
<html lang="en">
<head>
<meta charset="utf-8">
<title>KVT Legal – Business Cards</title>
<link href="https://fonts.googleapis.com/css2?family=Nunito+Sans:wght@400;600;700;800&display=swap" rel="stylesheet">
<style>
  :root {
    --stage: #2b2b2b;
    --card: #1b1b1b;
    --accent: #c4203f;
    --ink: #ffffff;
    --ink-soft: #e6e6e6;
  }
  * { box-sizing: border-box; margin: 0; padding: 0; }
  html, body {
    width: 1200px; height: 900px; overflow: hidden;
    background: var(--stage);
    font-family: "Nunito Sans", "Avenir", sans-serif;
  }
  .canvas {
    position: relative; width: 1200px; height: 900px;
  }
  .card {
    position: absolute; left: 320px; width: 560px; height: 320px;
    background: var(--card); border-radius: 16px;
    box-shadow: 0 6px 18px rgba(0,0,0,0.45);
    overflow: hidden;
  }
  .card--back { top: 110px; }
  .card--front { top: 470px; }

  .brand {
    display: flex; align-items: center; gap: 14px;
    color: var(--ink); font-weight: 800; letter-spacing: 1px;
  }
  .brand__mark { background: var(--accent); display: block; }

  .card--back .brand {
    position: absolute; left: 50%; top: 50%;
    transform: translate(-50%, -50%);
    font-size: 44px;
  }
  .card--back .brand__mark { width: 38px; height: 38px; }

  .card--front .brand {
    position: absolute; left: 40px; top: 96px;
    font-size: 22px; gap: 10px;
  }
  .card--front .brand__mark { width: 20px; height: 20px; }

  .divider {
    position: absolute; left: 40px; right: 40px; top: 172px;
    height: 1.5px; background: var(--accent);
  }

  .person {
    position: absolute; right: 40px; top: 96px; text-align: right;
  }
  .person__name {
    color: var(--accent); font-weight: 700; font-size: 22px; letter-spacing: 0.3px;
  }
  .person__role {
    color: var(--ink); font-size: 13px; margin-top: 4px;
  }

  .address {
    position: absolute; right: 40px; top: 188px; text-align: right;
    color: var(--ink-soft); font-size: 12px; line-height: 1.5;
  }

  .contacts {
    position: absolute; left: 40px; top: 192px; list-style: none;
    color: var(--ink); font-size: 14px; letter-spacing: 1px; line-height: 24px;
  }
  .contacts li { display: flex; align-items: center; gap: 12px; }
  .contacts svg { width: 12px; height: 12px; fill: var(--accent); flex: none; }
</style>
</head>
<body>
<main class="canvas">

  <section class="card card--back" aria-label="Card back">
    <div class="brand">
      <span class="brand__mark"></span>
      <span class="brand__name">KVT LEGAL</span>
    </div>
  </section>

  <section class="card card--front" aria-label="Card front">
    <div class="brand">
      <span class="brand__mark"></span>
      <span class="brand__name">KVT LEGAL</span>
    </div>

    <div class="person">
      <p class="person__name">Boris Telemark</p>
      <p class="person__role">Partner</p>
    </div>

    <div class="divider"></div>

    <ul class="contacts">
      <li>
        <svg viewBox="0 0 24 24" aria-hidden="true"><path d="M6.6 10.8a15.1 15.1 0 0 0 6.6 6.6l2.2-2.2a1 1 0 0 1 1-.25 11.4 11.4 0 0 0 3.6.57 1 1 0 0 1 1 1V20a1 1 0 0 1-1 1A17 17 0 0 1 3 4a1 1 0 0 1 1-1h3.5a1 1 0 0 1 1 1c0 1.25.2 2.45.57 3.57a1 1 0 0 1-.25 1z"/></svg>
        0438 715 642
      </li>
      <li>
        <svg viewBox="0 0 24 24" aria-hidden="true"><path d="M2 5h20v14H2z M2 5l10 7 10-7" fill-rule="evenodd"/><path d="M3 6.5l9 6.3 9-6.3V18H3z" fill="#1b1b1b" opacity="0"/></svg>
        boris@kvtlaw.co
      </li>
      <li>
        <svg viewBox="0 0 24 24" aria-hidden="true"><circle cx="12" cy="12" r="10"/></svg>
        www.kvtlaw.co
      </li>
    </ul>

    <address class="address" style="font-style:normal">
      Level 3, 118 Wexbury<br>
      Street Sydney NSW 2000
    </address>
  </section>

</main>
</body>
</html>
```